Introduction of new dentist and new treatments

We want inform our Patients of our new dentist and new treatment methods. It is dealing about biologic dentistry and holistic dentistry. we are in switzerland and speak german

Font styles to use
Sans Serif

Colors
00a990
33b8a4
9bcb3c
acd036
cadf82
0292cd
3176b5
e34297
e667a6

Requirements
Must have
• Text, which can be edited. It will be in german
• Name of the dental clinic is
• "Brivana - Ihr Zahnarzt in Zug"
Nice to have
• A4 Layout

```html
<!DOCTYPE html>
<html lang="de">
<head>
<meta charset="utf-8">
<title>Brivana – Ihr Zahnarzt in Zug</title>
<link href="https://fonts.googleapis.com/css2?family=Lato:wght@400;700;900&display=swap" rel="stylesheet">
<style>
  :root {
    --sky-light: #e8f6fd;
    --sky-mid: #9fdaf3;
    --teal-photo: #3fb9d6;
    --brand-blue: #21a5df;
    --column-blue: #23a8e0;
    --brand-green: #47b354;
    --deep-green: #139a50;
    --ink: #333a40;
    --white: #ffffff;
  }
  * { box-sizing: border-box; margin: 0; padding: 0; }
  html, body { width: 901px; height: 1200px; overflow: hidden; background: var(--white); }
  body { font-family: "Lato", Arial, sans-serif; color: var(--ink); }

  .flyer { position: relative; width: 901px; height: 1200px; overflow: hidden; background: var(--white); }
  .flyer__art { position: absolute; inset: 0; }

  .brand { position: absolute; left: 500px; top: 160px; width: 340px; color: #2e3338; }
  .brand__name { font-weight: 700; font-size: 62px; line-height: 1; letter-spacing: 0.5px; }
  .brand__tagline { font-weight: 700; font-size: 28px; line-height: 1.2; margin-top: 6px; color: #2e3338; }

  .headline {
    position: absolute; left: 30px; top: 418px; width: 450px;
    text-align: center; color: var(--brand-green);
    font-weight: 900; font-size: 32px; line-height: 41px;
  }

  .section { position: absolute; }
  .section--left { left: 60px; width: 430px; }
  .section--right { left: 559px; width: 300px; color: var(--white); }

  .section__title--blue { color: var(--brand-blue); font-weight: 700; font-size: 25px; line-height: 24px; margin-bottom: 14px; }
  .section__title--caps { font-weight: 900; font-size: 25px; line-height: 31px; text-transform: uppercase; margin-bottom: 18px; }

  .section__body { font-size: 13.6px; line-height: 17.1px; }

  .s1 { top: 660px; }
  .s2 { top: 918px; }
  .s3 { top: 590px; }
  .s4 { top: 866px; }
</style>
</head>
<body>
<main class="flyer">
  <svg class="flyer__art" width="901" height="1200" viewBox="0 0 901 1200" aria-hidden="false">
    <defs>
      <linearGradient id="headerSky" x1="0" y1="0" x2="1" y2="1">
        <stop offset="0" stop-color="#2fb2d3"/>
        <stop offset="0.45" stop-color="#9fdaf3"/>
        <stop offset="0.7" stop-color="#e8f6fd"/>
        <stop offset="1" stop-color="#5cc0ec"/>
      </linearGradient>
      <linearGradient id="leftFade" x1="0" y1="0" x2="0" y2="1">
        <stop offset="0" stop-color="#e9eef1"/>
        <stop offset="1" stop-color="#ffffff"/>
      </linearGradient>
    </defs>

    <rect x="0" y="0" width="901" height="440" fill="url(#headerSky)" role="img"
          aria-label="Foto: Zahnmodell, Stethoskop, Zahnbürste und Zahnspiegel auf hellblauem Hintergrund"/>

    <rect x="0" y="380" width="512" height="260" fill="url(#leftFade)"/>
    <rect x="512" y="400" width="389" height="800" fill="var(--column-blue)"/>

    <path d="M0,332 C170,300 360,320 540,356 C690,384 800,388 901,384 L901,395 C800,398 690,394 540,366 C360,332 170,312 0,344 Z" fill="var(--white)"/>
    <path d="M0,344 C170,312 360,332 540,366 C690,394 800,398 901,395 L901,545 C780,520 660,462 530,420 C380,378 190,372 0,408 Z" fill="var(--brand-green)"/>
    <path d="M300,372 C430,385 560,400 700,430 C790,450 850,458 901,460 L901,545 C780,520 660,462 530,420 C460,398 380,382 300,372 Z" fill="var(--deep-green)"/>
    <path d="M0,408 C190,372 380,378 530,420 C660,462 780,520 901,545 L901,560 C780,538 660,478 530,436 C380,392 190,388 0,424 Z" fill="var(--white)"/>
  </svg>

  <header class="brand">
    <div class="brand__name">Brivana</div>
    <div class="brand__tagline">Ihr Zahnarzt in Zug</div>
  </header>

  <h1 class="headline">Interdisziplinäre Zahnmedizin- Zusammenhang zwischen Zahnproblemen und der Gesundheit von Körper und Geist</h1>

  <section class="section section--left s1">
    <h2 class="section__title--blue">Funktion des Kauorgans und interdisziplinäre Zahnmedizin</h2>
    <p class="section__body">„Funktion ist nicht alles. Aber ohne Funktion ist alles nichts!“ Sagte einst Prof. A. Lindner (Zahnarzt, Gnathologie) und betonte die Bedeutung der Funktion des Kausystems. Sprechen, Kauen aber auch Körperhaltung und Stressmanagement gehören zu den Funktionen der Zähne. Ein gut funktionierendes Kauorgan (nach Prof. R. Harteneck, interdisziplinäre Zahnmedizin) kann Stress bewältigen und mehr Leistung und Wohlbefinden bringen. Sehr oft erkennt man Funktionsstörungen daran, dass die Zähne nicht richtig zueinander passen oder Muskelverspannungen und Schmerzen im Kiefergelenk auftreten.</p>
  </section>

  <section class="section section--left s2">
    <h2 class="section__title--blue">Parodontitis und systemische Erkrankungen</h2>
    <p class="section__body">Parodontitis (Entzündung des Zahnhalteapparats) ist eine der häufigsten chronischen Krankheiten weltweit und daher gut erforscht. Herzkrankheiten, Diabetes und Frühgeburtlichkeit sind einige der systemischen Krankheiten mit der Parodontitis in Zusammenhang steht. Zahnfleischbluten, Zahnlockerung, Zahnfleischschwund und Zahnverlust sind typische Begleiterscheinungen von Parodontitis. Eine systematische Parodontitis-Behandlung kann auch positive Auswirkungen auf die gesamte Gesundheit haben.</p>
  </section>

  <section class="section section--right s3">
    <h2 class="section__title--caps">Zahnverlust und neurologische Auswirkung</h2>
    <p class="section__body">Ein physiologisches Kausystem hat sehr feine Steuerungs- und Wahrnehmungsmöglichkeiten. Bei Zahnverlust werden diese Fähigkeiten weniger benötigt. Weniger gebrauchte Ressourcen werden von der Natur dementsprechend abgebaut. Studien zeigen, dass Menschen mit weniger Zähnen mehr Risiko zur Bildung von Demenz bergen.</p>
  </section>

  <section class="section section--right s4">
    <h2 class="section__title--caps">Ganzheitliche Erklärungen</h2>
    <p class="section__body">Die komplementäre Zahnheilkunde, sehr oft auch als ganzheitliche oder biologische Zahnheilkunde bezeichnet, versucht mit Hilfe von Meridianen (Traditionelle Chinesische Medizin), den Zusammenhang zwischen Zähnen und anderen Organen und Körperteilen zu erklären. Es gibt immer mehr Patienten und Zahnärzte die von dieser Theorie und deren Ergebnissen überzeugt sind. Aufgrund der wissenschaftlichen Lage ist eine ausführliche Aufklärung vor der Behandlung sehr ratsam</p>
  </section>
</main>
</body>
</html>
```